Graphic design for an existing cardboard Archive box

We need a graphic design for an existing archive box packaging.
Our request is really simple: we would like to have a graphic design that is pleasant to put in the office or on the bookshelf in the living room.
The project must be in CMYK color space, no other colors (Pantone, spot colors, metallic inks, ecc) or varnishes can be used.
You can see and download some sample pictures and the complete flat template in Adobe Illustrator, EPS, and PDF file.

Target Market(s)

Both individual customers and professional

Industry/Entity Type

Graphic Design

Requirements
Must have
• REALLY IMPORTANT: we'd like to see 2 files: "flat graphic" on the template and applied on the 3D. Thank you

Graphic design that is pleasant to put in the office or on the bookshelf in the living room.

CMYK color space only.

We like colorful images, positive and tempting graphics.

```html
<!DOCTYPE html>
<html lang="en">
<head>
<meta charset="utf-8">
<title>Archive Box – Flat Graphic Layout</title>
<link rel="stylesheet" href="https://fonts.googleapis.com/css2?family=Inter:wght@400&display=swap">
<style>
  :root {
    --page: #e9e9e9;
    --sheet: #ffffff;
    --trim: #b9b9b9;
    --cyan: #00ffff;
    --magenta: #ff00ff;
    --yellow: #ffff00;
    --black: #000000;
    --paper: #ffffff;
  }
  html, body {
    margin: 0;
    padding: 0;
    overflow: hidden;
  }
  body {
    width: 1200px;
    height: 806px;
    background: radial-gradient(ellipse at center, var(--sheet) 60%, var(--page) 100%);
    position: relative;
    font-family: "Inter", sans-serif;
  }
  .sheet {
    position: absolute;
    left: 70px;
    top: 34px;
    width: 1058px;
    height: 736px;
    background: var(--sheet);
    box-shadow: 0 0 22px rgba(0, 0, 0, 0.18);
  }
  .panel {
    position: absolute;
    box-sizing: border-box;
    border: 1px solid var(--trim);
    overflow: hidden;
  }
  /* Box faces, positioned within the sheet */
  .panel--top-flap {
    left: 117px; top: 23px; width: 272px; height: 83px;
    background: linear-gradient(100deg, var(--paper) 8%, var(--magenta) 14%, var(--magenta) 48%, var(--black) 52%, var(--black) 70%, var(--magenta) 74%, var(--paper) 90%);
  }
  .panel--left-side {
    left: 24px; top: 113px; width: 80px; height: 370px;
    background: linear-gradient(160deg, var(--cyan) 0%, var(--magenta) 22%, var(--cyan) 40%, var(--cyan) 60%, var(--black) 68%, var(--cyan) 74%, var(--paper) 96%);
  }
  .panel--front {
    left: 116px; top: 113px; width: 271px; height: 377px;
    background: linear-gradient(150deg, var(--magenta) 0%, var(--cyan) 25%, var(--black) 45%, var(--cyan) 58%, var(--black) 75%, var(--yellow) 85%, var(--yellow) 100%);
  }
  .panel--bottom-flap {
    left: 116px; top: 498px; width: 275px; height: 82px;
    background: linear-gradient(90deg, var(--paper) 8%, var(--black) 12%, var(--black) 66%, var(--yellow) 70%, var(--paper) 95%);
  }
  .panel--narrow-side {
    left: 396px; top: 112px; width: 87px; height: 375px;
    background: linear-gradient(180deg, var(--magenta) 0%, var(--black) 20%, var(--paper) 40%, var(--cyan) 52%, var(--yellow) 70%, var(--paper) 80%, var(--yellow) 100%);
  }
  .panel--back {
    left: 495px; top: 112px; width: 274px; height: 375px;
    background: linear-gradient(140deg, var(--black) 0%, var(--magenta) 25%, var(--black) 33%, var(--cyan) 50%, var(--magenta) 68%, var(--paper) 78%, var(--yellow) 92%);
  }
  .spine-row {
    position: absolute;
    left: 793px;
    top: 478px;
    display: flex;
    gap: 7px;
  }
  .panel--spine {
    position: relative;
    width: 58px;
    height: 251px;
    background: linear-gradient(180deg, var(--magenta) 0%, var(--black) 14%, var(--cyan) 26%, var(--paper) 38%, var(--yellow) 48%, var(--yellow) 68%, var(--paper) 72%, var(--paper) 94%, var(--yellow) 100%);
  }
</style>
</head>
<body>
  <main class="sheet">
    <div class="panel panel--top-flap" role="img" aria-label="Top flap: abstract magenta, black and cyan hand-drawn shapes"></div>
    <div class="panel panel--left-side" role="img" aria-label="Left side panel: cyan and magenta abstract blocks with a black triangle"></div>
    <div class="panel panel--front" role="img" aria-label="Front panel: bold abstract composition in cyan, magenta, yellow and black with outlined blocks and a diagonal black triangle"></div>
    <div class="panel panel--bottom-flap" role="img" aria-label="Bottom flap: black block outlined in yellow beside a yellow shape"></div>
    <div class="panel panel--narrow-side" role="img" aria-label="Narrow side panel: abstract shapes with a drawn label sheet on yellow"></div>
    <div class="panel panel--back" role="img" aria-label="Back panel: black bar, magenta triangle, cyan steps and a yellow band"></div>
    <div class="spine-row">
      <div class="panel panel--spine" role="img" aria-label="Spine variant with abstract CMYK shapes and a drawn label sheet"></div>
      <div class="panel panel--spine" role="img" aria-label="Spine variant with abstract CMYK shapes and a drawn label sheet"></div>
      <div class="panel panel--spine" role="img" aria-label="Spine variant with abstract CMYK shapes and a drawn label sheet"></div>
      <div class="panel panel--spine" role="img" aria-label="Spine variant with abstract CMYK shapes and a drawn label sheet"></div>
    </div>
  </main>
</body>
</html>
```